Kip Moor! Then Where?, Bail Bond Company Check-in App , Court date, Court Reminders, Payments

Kip Moor!
Then Where?
WINNER OF THIS CONTEST WILL HAVE OPPORTUNITY TO DESIGN CUSTOMIZE SOME OUR COMPANY PAGES AFTER CONTEST!
Check-in with your Bail agent via pic/video
Receive Court reminders
Make a payments

Basically this app is a portal to 3rd party bail companies.
The idea is for the person whom makes bail downloads the KipMoor app from Plaza Shelf.
Then they select a bail bond company.
This would be similar to a restaurant, real estate agent, insurance agent,,app where we could populate bail bond companies by client location or by typing in name of bail company.
We would like the ability to customize each bail bond company landing pages but are open to a global concept. when you click the bail bond company location it would have the logos for that company so the bail bond company screens would need to be customizeble
The app will require a photo or video check-in that is date and time
stamped with a gps location stored in check-in history
Check-in can be scheduled or random or voluntary
Voluntary and Scheduled Check-ins would require check-in button
Random would be via alert or text

The app should be able to receive court date updates
The app should allow clients to make payments to bail bond company
we need
KIP MOOR! landing page
client registration screens, check-in screens, available bail bond company screens for client to choose from
client registration page should include
name
email address
phone number
picture
home address
work address
date of birth
this app is different from our z-lumo app. this is a bail bond check-in app for third party bail bond companies.
landing page should be KIP MOOR! Then Where?
KIP MOOR ! Registration
Find your bail bond Company should list bail bond companies near me and search bar for searching bail bond companies by name
Next landing pages would be customizable for the third party bail bond companies
these would include pages for
check-ins via pics/videos
payment page
court reminders
contact information for bail bond companies
Zorva Bail Pages include
initial landing page
registration page
search bail companies

Bail bond company pages should include
Bali bond company landing page
Use ORVAL BAIL BOND COMPANY as example
contact information for bail company
check-in page
payment page
court reminder page

Low designer entries

Low designer entries

Sick

Sick

Sick

Target Market(s)

Court Defendants, Probation ,jails, sheriffs, judges, attorneys

Industry/Entity Type

justice, law enforcement, courts,

Requirements
Must have
• Check-in via pic/video, ability to receive court date reminders, make paymentswe need client registration screens, check-in screens, available bail bond company screens for client to choose from
Nice to have
• Professional easy to navigate intuitive customizable to 3rd party bail bond companies, logos,phone numbers etc.
Should not have
• unprofessional graphics,

```html
<!DOCTYPE html>
<html lang="en">
<head>
<meta charset="utf-8">
<title>Zorva Bail – App Screens</title>
<link href="https://fonts.googleapis.com/css2?family=Tinos:wght@400;700&family=Roboto:wght@400;500&display=swap" rel="stylesheet">
<style>
:root{
  --stage:#a1a1a1;
  --screen:#ffffff;
  --ink:#111111;
  --muted:#6f6f6f;
  --soft:#e6e6e6;
  --card:#ebebeb;
  --line:#4a4a4a;
  --photo-a:#3b4656;
  --photo-b:#c9d6df;
}
*{box-sizing:border-box;margin:0;padding:0}
html,body{width:1200px;height:2519px;overflow:hidden;background:var(--stage)}
.canvas{width:1227px;height:2576px;position:relative;transform:scale(.978);transform-origin:0 0;background:var(--stage);font-family:"Roboto",sans-serif;color:var(--ink)}
.screen{position:absolute;width:384px;height:832px;background:var(--screen);overflow:hidden}
.abs{position:absolute}
.serif{font-family:"Tinos",serif}
.center{left:0;right:0;text-align:center}
.title{font-family:"Tinos",serif;font-weight:700;font-size:24px}
.hline{height:1px;background:var(--line)}
.btn-outline{border:2px solid var(--ink);border-radius:26px;display:flex;align-items:center;justify-content:center;font-family:"Tinos",serif;font-weight:700;font-size:16px;background:transparent}
.btn-solid{background:var(--ink);color:#fff;border-radius:26px;display:flex;align-items:center;justify-content:center;font-family:"Tinos",serif;font-size:18px}
.muted{color:var(--muted)}
.logo-disc{width:116px;height:116px;border-radius:50%;background:#fff;box-shadow:0 4px 14px rgba(0,0,0,.12);display:flex;align-items:center;justify-content:center;font-family:"Tinos",serif;font-weight:700;font-size:16px}
.co-title{font-family:"Tinos",serif;font-size:19px}
.co-loc{font-size:16px;display:flex;align-items:center;gap:8px}
.co-desc{font-size:12px;line-height:21px;color:#555}
.expand{width:26px;height:26px;border-radius:50%;background:#fff;box-shadow:0 2px 6px rgba(0,0,0,.15);display:flex;align-items:center;justify-content:center}
.field-label{font-size:13px;background:#fff;padding:0 6px}
.field{border:1px solid #ddd;border-radius:22px;height:42px;width:243px}
.field-icon{width:26px;height:26px;border-radius:50%;background:#ddd;display:flex;align-items:center;justify-content:center}
.chip{height:46px;border-radius:23px;border:1px solid var(--ink);display:flex;align-items:center;justify-content:center;font-family:"Tinos",serif;font-size:16px}
.row-label{font-family:"Tinos",serif;font-weight:700;font-size:17px}
.contact-ring{width:52px;height:52px;border:2px solid var(--ink);border-radius:50%;display:flex;align-items:center;justify-content:center}
.rem-title{font-family:"Tinos",serif;font-weight:700;font-size:19px}
.rem-sub{font-size:13px}
.radio{width:20px;height:20px;border:1.5px solid #333;border-radius:50%;display:flex;align-items:center;justify-content:center}
</style>
</head>
<body>
<svg width="0" height="0" style="position:absolute">
  <defs>
    <symbol id="i-back" viewBox="0 0 20 20"><path d="M13 3 6 10l7 7" fill="none" stroke="currentColor" stroke-width="2"/></symbol>
    <symbol id="i-down" viewBox="0 0 20 20"><path d="M5 8l5 5 5-5" fill="none" stroke="currentColor" stroke-width="2"/></symbol>
    <symbol id="i-user" viewBox="0 0 20 20"><circle cx="10" cy="10" r="9" fill="none" stroke="currentColor" stroke-width="1.6"/><circle cx="10" cy="8" r="3.2" fill="currentColor"/><path d="M4.5 15.5c1.5-3 9.5-3 11 0" fill="currentColor"/></symbol>
    <symbol id="i-pin" viewBox="0 0 20 20"><path d="M10 1a6 6 0 0 0-6 6c0 5 6 12 6 12s6-7 6-12a6 6 0 0 0-6-6z" fill="currentColor"/><circle cx="10" cy="7" r="2.2" fill="#fff"/></symbol>
    <symbol id="i-phone" viewBox="0 0 20 20"><path d="M5 2l3 3-2 3c1 2 3 4 5 5l2-2 3 3-2 3C8 17 3 12 2 5z" fill="currentColor"/></symbol>
    <symbol id="i-mail" viewBox="0 0 20 20"><rect x="2" y="4" width="16" height="12" rx="1.5" fill="currentColor"/><path d="M2.5 5 10 11l7.5-6" fill="none" stroke="#fff" stroke-width="1.5"/></symbol>
    <symbol id="i-lock" viewBox="0 0 20 20"><rect x="4" y="9" width="12" height="9" rx="1.5" fill="currentColor"/><path d="M6.5 9V6.5a3.5 3.5 0 0 1 7 0V9" fill="none" stroke="currentColor" stroke-width="2"/></symbol>
    <symbol id="i-lock-o" viewBox="0 0 20 20"><rect x="4.5" y="9" width="11" height="9" rx="1.5" fill="none" stroke="currentColor" stroke-width="1.4"/><path d="M7 9V6.5a3 3 0 0 1 6 0V9" fill="none" stroke="currentColor" stroke-width="1.4"/></symbol>
    <symbol id="i-person" viewBox="0 0 20 20"><circle cx="10" cy="6" r="3.5" fill="currentColor"/><path d="M4 18c0-5 12-5 12 0z" fill="currentColor"/></symbol>
    <symbol id="i-bell" viewBox="0 0 20 20"><path d="M10 2a5 5 0 0 0-5 5v5l-2 3h14l-2-3V7a5 5 0 0 0-5-5z" fill="currentColor"/><circle cx="10" cy="17.5" r="1.8" fill="currentColor"/><circle cx="16" cy="4" r="2.6" fill="currentColor"/></symbol>
    <symbol id="i-cal" viewBox="0 0 20 20"><rect x="2" y="4" width="16" height="14" fill="none" stroke="currentColor" stroke-width="1.4"/><path d="M2 8h16M6 2v4M14 2v4M5 11h10M5 14h10M8 8v10M12 8v10" stroke="currentColor" stroke-width="1"/></symbol>
    <symbol id="i-tick" viewBox="0 0 20 20"><path d="M5 10l3.5 3.5L15 7" fill="none" stroke="currentColor" stroke-width="2"/></symbol>
    <symbol id="i-mark" viewBox="0 0 20 20"><path d="M5 2h10v16l-5-4-5 4z" fill="currentColor"/></symbol>
  </defs>
</svg>

<div class="canvas">

  <!-- Login -->
  <section class="screen" style="left:18px;top:17px">
    <h1 class="abs center serif" style="top:185px;font-size:50px;font-weight:700">Zorva Bail</h1>
    <div class="abs muted" style="left:39px;top:336px;font-size:17px">Username</div>
    <svg class="abs" style="left:322px;top:337px;width:16px;height:16px;color:#777"><use href="#i-lock-o"/></svg>
    <div class="abs hline" style="left:41px;top:377px;width:302px"></div>
    <div class="abs muted" style="left:39px;top:460px;font-size:17px">Password</div>
    <svg class="abs" style="left:322px;top:460px;width:16px;height:16px;color:#555"><use href="#i-lock"/></svg>
    <div class="abs hline" style="left:41px;top:500px;width:302px"></div>
    <div class="abs btn-outline" style="left:76px;top:568px;width:232px;height:47px">LOG IN</div>
  </section>

  <!-- Company list -->
  <section class="screen" style="left:421px;top:17px">
    <svg class="abs" style="left:40px;top:83px;width:20px;height:20px"><use href="#i-back"/></svg>
    <div class="abs center title" style="top:79px">Zorva Bail</div>
    <svg class="abs" style="left:321px;top:84px;width:21px;height:21px;color:#777"><use href="#i-user"/></svg>
    <div class="abs center serif" style="top:143px;font-size:21px;font-weight:700">List of Company</div>

    <div class="abs logo-disc" style="left:33px;top:223px">Norvale</div>
    <div class="abs co-title" style="left:177px;top:202px">Lorem ipsum dolor sit</div>
    <div class="abs co-loc" style="left:175px;top:239px"><svg style="width:15px;height:15px"><use href="#i-pin"/></svg>Lorem ipsum<svg style="width:13px;height:13px"><use href="#i-down"/></svg></div>
    <div class="abs co-desc" style="left:177px;top:274px">Lorem ipsum dolor sit amet,<br>consectetur adipiscing</div>
    <div class="abs expand" style="left:178px;top:331px"><svg style="width:14px;height:14px"><use href="#i-down"/></svg></div>

    <div class="abs" style="left:0;top:380px;width:384px;height:208px;background:var(--soft)"></div>
    <div class="abs logo-disc" style="left:33px;top:424px">Tessary</div>
    <div class="abs co-title" style="left:177px;top:403px">Lorem ipsum dolor sit</div>
    <div class="abs co-loc" style="left:175px;top:440px"><svg style="width:15px;height:15px"><use href="#i-pin"/></svg>Lorem ipsum<svg style="width:13px;height:13px"><use href="#i-down"/></svg></div>
    <div class="abs co-desc" style="left:177px;top:475px">Lorem ipsum dolor sit amet,<br>consectetur adipiscing</div>
    <div class="abs expand" style="left:178px;top:532px"><svg style="width:14px;height:14px"><use href="#i-down"/></svg></div>

    <div class="abs logo-disc" style="left:33px;top:635px;font-size:14px">Brightwell</div>
    <div class="abs co-title" style="left:177px;top:614px">Lorem ipsum dolor sit</div>
    <div class="abs co-loc" style="left:175px;top:651px"><svg style="width:15px;height:15px"><use href="#i-pin"/></svg>Lorem ipsum<svg style="width:13px;height:13px"><use href="#i-down"/></svg></div>
    <div class="abs co-desc" style="left:177px;top:686px">Lorem ipsum dolor sit amet,<br>consectetur adipiscing</div>
    <div class="abs expand" style="left:178px;top:743px"><svg style="width:14px;height:14px"><use href="#i-down"/></svg></div>
    <div class="abs" style="left:32px;top:799px;width:321px;height:1px;background:#ccc"></div>
  </section>

  <!-- Company landing -->
  <section class="screen" style="left:824px;top:17px">
    <div class="abs title" style="left:41px;top:66px">Zorva Bail</div>
    <svg class="abs" style="left:287px;top:70px;width:20px;height:20px;color:#777"><use href="#i-bell"/></svg>
    <svg class="abs" style="left:322px;top:70px;width:21px;height:21px;color:#777"><use href="#i-user"/></svg>
    <div class="abs" role="img" aria-label="Photo of business people reviewing financial charts on a tablet" style="left:0;top:116px;width:384px;height:217px;border-radius:40px;background:linear-gradient(135deg,var(--photo-a),#7d8fa0 45%,var(--photo-b))"></div>
    <div class="abs center title" style="top:357px">Tessary</div>
    <div class="abs center" style="top:401px;font-size:13px;display:flex;justify-content:center;gap:8px;align-items:center"><svg style="width:13px;height:13px"><use href="#i-phone"/></svg>+1 (555) 010 2040</div>
    <div class="abs center" style="top:434px;font-size:12px;line-height:21px;padding:0 40px">Lorem ipsum dolor sit amet, consectetur adipiscing elit, sed do eiusmod tempor</div>
    <div class="abs serif" style="left:42px;top:498px;font-size:19px">Check in time</div>
    <div class="abs muted" style="left:222px;top:501px;font-size:13px;display:flex;gap:12px;align-items:center"><svg style="width:15px;height:15px;color:#777"><use href="#i-cal"/></svg>20 / 11 / 20222</div>
    <div class="abs btn-outline" style="left:101px;top:548px;width:183px;height:50px;font-size:18px">CHECK-IN</div>
    <div class="abs serif" style="left:38px;top:627px;font-size:17px;display:flex;gap:10px;align-items:center"><svg style="width:15px;height:15px"><use href="#i-pin"/></svg>Lorem ipsum dolor sit amet, consectetur</div>
    <div class="abs center" style="top:662px;font-size:10px;line-height:20px;padding:0 50px">Lorem ipsum dolor sit amet, consectetur adipiscing elit, sed do eiusmod tempor incididunt ut labore.</div>
    <div class="abs btn-outline" style="left:91px;top:720px;width:203px;height:50px">MAKE A PAYMENTS</div>
  </section>

  <!-- Registration -->
  <section class="screen" style="left:18px;top:868px">
    <svg class="abs" style="left:39px;top:108px;width:20px;height:20px"><use href="#i-back"/></svg>
    <div class="abs center title" style="top:103px">Zorva Bail</div>
    <svg class="abs" style="left:320px;top:108px;width:21px;height:21px;color:#777"><use href="#i-user"/></svg>
    <div class="abs center serif" style="top:175px;font-size:22px;font-weight:700">Registration</div>

    <div class="abs field" style="left:71px;top:249px"></div><div class="abs field-label" style="left:97px;top:240px">Full Name</div>
    <div class="abs field-icon" style="left:281px;top:257px"><svg style="width:12px;height:12px;color:#444"><use href="#i-person"/></svg></div>
    <div class="abs field" style="left:71px;top:330px"></div><div class="abs field-label" style="left:97px;top:321px">Email Address</div>
    <div class="abs field-icon" style="left:281px;top:338px"><svg style="width:12px;height:12px;color:#444"><use href="#i-mail"/></svg></div>
    <div class="abs field" style="left:71px;top:412px"></div><div class="abs field-label" style="left:97px;top:403px">Phone Number</div>
    <div class="abs field-icon" style="left:281px;top:420px"><svg style="width:12px;height:12px;color:#444"><use href="#i-phone"/></svg></div>
    <div class="abs field" style="left:71px;top:493px"></div><div class="abs field-label" style="left:97px;top:484px">Password</div>
    <div class="abs field-icon" style="left:281px;top:501px"><svg style="width:12px;height:12px;color:#444"><use href="#i-lock"/></svg></div>
    <div class="abs field" style="left:71px;top:574px"></div><div class="abs field-label" style="left:97px;top:565px">Confirm Password</div>
    <div class="abs field-icon" style="left:281px;top:582px"><svg style="width:14px;height:14px"><circle cx="7" cy="7" r="6" fill="#444"/><path d="M4 7l2 2 4-4" stroke="#fff" fill="none" stroke-width="1.5"/></svg></div>

    <div class="abs" style="left:71px;top:638px;width:13px;height:13px;background:var(--ink);border-radius:2px"><svg style="width:13px;height:13px;color:#fff;display:block"><use href="#i-tick"/></svg></div>
    <div class="abs muted" style="left:100px;top:636px;font-size:14px">Agree with <b style="color:var(--ink);font-weight:500">Term &amp; Conditions</b></div>
    <div class="abs btn-solid" style="left:71px;top:693px;width:243px;height:47px;font-weight:700;font-size:17px">REGISTER</div>
    <div class="abs center muted" style="top:756px;font-size:14px">Already have an account? <b style="color:var(--ink);font-weight:500">Login</b></div>
  </section>

  <!-- Check-in -->
  <section class="screen" style="left:421px;top:868px;background:var(--soft)">
    <svg class="abs" style="left:40px;top:100px;width:20px;height:20px"><use href="#i-back"/></svg>
    <div class="abs center title" style="top:95px">Zorva Bail</div>
    <svg class="abs" style="left:321px;top:101px;width:21px;height:21px;color:#777"><use href="#i-user"/></svg>
    <svg class="abs" style="left:160px;top:155px;width:66px;height:60px"><rect x="3" y="9" width="46" height="46" rx="5" fill="none" stroke="#888" stroke-width="5"/><path d="M14 30l12 12L62 6" fill="none" stroke="#888" stroke-width="8"/></svg>
    <div class="abs center serif" style="top:220px;font-size:17px;color:#888">Check-in</div>
    <div class="abs chip" style="left:21px;top:265px;width:110px;background:var(--ink);color:#fff">Scheduled</div>
    <div class="abs chip" style="left:142px;top:265px;width:104px">Random</div>
    <div class="abs chip" style="left:260px;top:265px;width:104px">Voluntary</div>
    <div class="abs" style="left:0;top:344px;width:384px;height:500px;background:var(--screen);border-radius:60px 60px 0 0"></div>
    <div class="abs serif" style="left:42px;top:378px;font-size:19px;font-weight:700">Date and Time</div>
    <div class="abs serif" style="left:41px;top:421px;font-size:16px;color:#333">Day</div>
    <div class="abs serif" style="left:90px;top:421px;font-size:16px;color:#333">Month</div>
    <div class="abs serif" style="left:156px;top:421px;font-size:16px;color:#333">Hour</div>
    <div class="abs serif" style="left:211px;top:421px;font-size:16px;color:#333">Minute</div>
    <div class="abs" style="left:44px;top:466px;font-size:14px;color:#aaa"><span class="abs" style="left:0">23</span><span class="abs" style="left:60px">11</span><span class="abs" style="left:120px">07</span><span class="abs" style="left:180px">59</span><span class="abs" style="left:238px">PM</span></div>
    <div class="abs" style="left:44px;top:496px;font-size:14px"><span class="abs" style="left:0">24</span><span class="abs" style="left:60px">11</span><span class="abs" style="left:120px">08</span><span class="abs" style="left:180px">00</span><span class="abs" style="left:238px">AM</span></div>
    <div class="abs" style="left:44px;top:526px;font-size:14px;color:#aaa"><span class="abs" style="left:0">25</span><span class="abs" style="left:60px">11</span><span class="abs" style="left:120px">09</span><span class="abs" style="left:180px">01</span></div>
    <div class="abs serif" style="left:42px;top:580px;font-size:19px;font-weight:700">Note</div>
    <div class="abs" style="left:41px;top:616px;width:302px;height:101px;border-radius:18px;background:#e1e1e1"></div>
    <div class="abs btn-solid" style="left:41px;top:744px;width:111px;height:46px;font-weight:700">SAVE</div>
  </section>

  <!-- Payments -->
  <section class="screen" style="left:824px;top:868px">
    <svg class="abs" style="left:40px;top:84px;width:20px;height:20px"><use href="#i-back"/></svg>
    <div class="abs center title" style="top:79px">Zorva Bail</div>
    <svg class="abs" style="left:318px;top:84px;width:21px;height:21px;color:#777"><use href="#i-user"/></svg>
    <div class="abs center serif" style="top:134px;font-size:19px;font-weight:700">Company Name</div>
    <div class="abs row-label" style="left:45px;top:180px">Next Payment</div>
    <div class="abs serif" style="left:45px;top:207px;font-size:28px;font-weight:700">$295.00</div>
    <div class="abs serif" style="left:46px;top:246px;font-size:11px">Due on : 9/5/2022</div>
    <div class="abs btn-solid" style="left:42px;top:289px;width:298px;height:47px">Make Payment</div>
    <div class="abs row-label" style="left:45px;top:367px">Last Payment</div>
    <div class="abs serif" style="left:45px;top:394px;font-size:12px">9/5/2022 &nbsp;&nbsp;10:00 PM</div>
    <div class="abs row-label" style="right:44px;top:371px;font-size:16px">$295.00</div>
    <div class="abs row-label" style="left:44px;top:447px">Current Balance</div>
    <div class="abs row-label" style="right:44px;top:450px;font-size:16px">$2295.00</div>
    <div class="abs hline" style="left:45px;top:501px;width:297px"></div>
    <div class="abs row-label" style="left:45px;top:532px">Court Date</div>
    <div class="abs serif" style="left:45px;top:559px;font-size:18px">Sep 8, 2023</div>
    <div class="abs row-label" style="right:44px;top:532px">Time</div>
    <div class="abs serif" style="right:44px;top:559px;font-size:18px">4:0 pm</div>
    <div class="abs hline" style="left:45px;top:608px;width:297px"></div>
    <div class="abs row-label" style="left:45px;top:645px;font-size:16px">Harlow Court</div>
    <div class="abs serif" style="left:45px;top:672px;font-size:15px;line-height:21px">1170 Wrenfield Street<br>Dunmore, MN 56011</div>
    <div class="abs btn-solid" style="left:42px;top:748px;width:298px;height:48px">Edit Court Info</div>
  </section>

  <!-- Contact -->
  <section class="screen" style="left:18px;top:1721px">
    <svg class="abs" style="left:39px;top:110px;width:20px;height:20px"><use href="#i-back"/></svg>
    <div class="abs center title" style="top:105px">Zorva Bail</div>
    <svg class="abs" style="left:320px;top:110px;width:21px;height:21px;color:#777"><use href="#i-user"/></svg>
    <div class="abs center serif" style="top:185px;font-size:25px;font-weight:700">Contact Information</div>
    <div class="abs contact-ring" style="left:36px;top:252px"><svg style="width:16px;height:16px"><use href="#i-pin"/></svg></div>
    <div class="abs contact-ring" style="left:168px;top:252px"><svg style="width:16px;height:16px"><use href="#i-phone"/></svg></div>
    <div class="abs contact-ring" style="left:299px;top:252px"><svg style="width:18px;height:18px"><use href="#i-mail"/></svg></div>
    <div class="abs serif" style="left:12px;width:100px;text-align:center;top:318px;font-size:19px">Address</div>
    <div class="abs serif" style="left:144px;width:100px;text-align:center;top:318px;font-size:19px">Phone</div>
    <div class="abs serif" style="left:275px;width:100px;text-align:center;top:318px;font-size:19px">Email</div>
    <div class="abs" style="left:2px;width:120px;text-align:center;top:354px;font-size:12px">Lorem ipsum do</div>
    <div class="abs" style="left:134px;width:120px;text-align:center;top:354px;font-size:12px">+1(555) 010 2040</div>
    <div class="abs" style="left:262px;width:124px;text-align:center;top:354px;font-size:12px">infozorvabail.com</div>
    <div class="abs muted" style="left:40px;top:424px;font-size:16px">Name</div><div class="abs hline" style="left:41px;top:460px;width:302px"></div>
    <div class="abs muted" style="left:40px;top:493px;font-size:16px">Phone</div><div class="abs hline" style="left:41px;top:530px;width:302px"></div>
    <div class="abs muted" style="left:40px;top:563px;font-size:16px">Email</div><div class="abs hline" style="left:41px;top:600px;width:302px"></div>
    <div class="abs muted" style="left:40px;top:632px;font-size:16px">Message</div><div class="abs hline" style="left:41px;top:669px;width:302px"></div>
    <div class="abs btn-outline" style="left:41px;top:695px;width:116px;height:50px">SUBMIT</div>
  </section>

  <!-- Court reminder -->
  <section class="screen" style="left:421px;top:1721px">
    <svg class="abs" style="left:40px;top:110px;width:20px;height:20px"><use href="#i-back"/></svg>
    <div class="abs center title" style="top:105px">Zorva Bail</div>
    <svg class="abs" style="left:321px;top:110px;width:21px;height:21px;color:#777"><use href="#i-user"/></svg>
    <svg class="abs" style="left:18px;top:168px;width:350px;height:90px"><path d="M4 80 L4 60 Q4 40 30 36 L275 4 Q300 2 310 20 L310 80 Z" fill="#7c7c7c"/><path d="M4 80 L4 55 Q4 30 30 30 L320 28 Q345 30 348 60 L348 80 Z" fill="#c7c7c7"/></svg>
    <div class="abs" style="left:18px;top:222px;width:349px;height:538px;border-radius:30px;background:var(--card)"></div>
    <div class="abs serif" style="left:36px;top:268px;font-size:22px">COURT REMINDER</div>
    <div class="abs serif" style="left:283px;top:266px;width:66px;height:29px;background:var(--ink);color:#fff;font-size:12px;font-weight:700;display:flex;align-items:center;justify-content:center">EDIT</div>

    <div class="abs radio" style="left:35px;top:335px"></div>
    <div class="abs rem-title" style="left:75px;top:333px">Lorem ipsum dolor sit</div>
    <svg class="abs" style="left:334px;top:336px;width:18px;height:18px"><use href="#i-mark"/></svg>
    <div class="abs rem-sub" style="left:74px;top:369px">Lorem ipsum dolor sit amet, consectetur</div>

    <div class="abs radio" style="left:35px;top:419px"></div>
    <div class="abs rem-title" style="left:75px;top:417px">Lorem ipsum dolor sit</div>
    <svg class="abs" style="left:334px;top:420px;width:18px;height:18px"><use href="#i-mark"/></svg>
    <div class="abs rem-sub" style="left:74px;top:453px">Lorem ipsum dolor sit amet, consectetur</div>

    <div class="abs radio" style="left:35px;top:503px"></div>
    <div class="abs rem-title" style="left:75px;top:501px">Lorem ipsum dolor sit</div>
    <svg class="abs" style="left:334px;top:504px;width:18px;height:18px"><use href="#i-mark"/></svg>
    <div class="abs rem-sub" style="left:74px;top:537px">Lorem ipsum dolor sit amet, consectetur</div>

    <div class="abs radio" style="left:35px;top:587px"><svg style="width:14px;height:14px"><use href="#i-tick"/></svg></div>
    <div class="abs rem-title" style="left:75px;top:585px">Lorem ipsum dolor sit</div>
    <div class="abs rem-sub" style="left:74px;top:621px">Lorem ipsum dolor sit amet, consectetur</div>

    <div class="abs radio" style="left:35px;top:671px"><svg style="width:14px;height:14px"><use href="#i-tick"/></svg></div>
    <div class="abs rem-title" style="left:75px;top:669px">Lorem ipsum dolor sit</div>
    <div class="abs rem-sub" style="left:74px;top:705px">Lorem ipsum dolor sit amet, consectetur</div>
  </section>

</div>
</body>
</html>
```